Construction Company

Design a clutter free business card, it can be double-sided utilizing the logo for BDN Ltd simple with all relevant contact information.

Please also a letterhead design to function for the purposes of invoicing, all mail requirements, with header to be distinctive while the footer ties page together and incorporates all necessary information.

For now, please use generic / dummy text and when a winner is selected, I will disclose the contact information.

Hi Designers! Please read the updated brief which includes the design of a business card and letterhead. Thank you!

```html
<!DOCTYPE html>
<html lang="en">
<head>
<meta charset="UTF-8">
<title>BDN Ltd – Business Card</title>
<link rel="stylesheet" href="https://fonts.googleapis.com/css2?family=Roboto:wght@400;500;700&display=swap">
<style>
  :root {
    --royal-blue: #0a3592;
    --ink-blue: #1f3f8f;
    --gold: #c1982a;
    --card-white: #ffffff;
    --backdrop: #e6e8ec;
    --soft-white: rgba(255,255,255,0.78);
  }
  * { box-sizing: border-box; margin: 0; padding: 0; }
  html, body {
    width: 1200px; height: 834px; overflow: hidden;
    background: var(--backdrop);
    font-family: "Roboto", Arial, sans-serif;
  }
  .canvas { position: relative; width: 1200px; height: 834px; }
  .card {
    position: absolute; left: 290px; width: 620px; height: 354px;
    border-radius: 4px; overflow: hidden;
    box-shadow: 0 6px 18px rgba(20,30,60,0.18);
  }
  .card-front { top: 45px; background: var(--card-white); }
  .card-back { top: 435px; background: var(--royal-blue); }

  .front-swoosh { position: absolute; inset: 0; width: 620px; height: 354px; }
  .front-logo {
    position: absolute; left: 48px; top: 64px;
    display: flex; align-items: center; gap: 10px;
    color: var(--royal-blue); font-weight: 500; font-size: 34px; letter-spacing: 2px;
  }
  .logo-dot { width: 14px; height: 14px; border-radius: 50%; background: var(--gold); }
  .divider {
    position: absolute; left: 250px; top: 52px; width: 1.5px; height: 150px;
    background: var(--ink-blue); opacity: 0.6;
  }
  .contact { position: absolute; left: 276px; top: 48px; color: var(--ink-blue); }
  .contact-name { color: var(--gold); font-weight: 700; font-size: 25px; }
  .contact-role { color: var(--ink-blue); font-size: 14px; margin-top: 2px; }
  .contact-address { font-size: 14px; margin-top: 10px; line-height: 1.3; }
  .contact-list { list-style: none; margin-top: 8px; font-size: 15px; }
  .contact-list li { display: flex; align-items: center; gap: 10px; line-height: 1.5; }
  .contact-list svg { width: 13px; height: 13px; flex: none; }

  .back-logo {
    position: absolute; left: 0; right: 0; top: 118px;
    display: flex; justify-content: center; align-items: center; gap: 16px;
    color: var(--card-white); font-weight: 500; font-size: 64px; letter-spacing: 4px;
  }
  .back-logo .logo-dot { width: 22px; height: 22px; }
  .back-web {
    position: absolute; left: 0; right: 0; bottom: 58px; text-align: center;
    color: var(--soft-white); font-size: 18px; letter-spacing: 0.5px;
  }
</style>
</head>
<body>
<main class="canvas">
  <section class="card card-front">
    <svg class="front-swoosh" viewBox="0 0 620 354" aria-hidden="true">
      <path d="M0 74 C60 264 330 284 620 308 L620 354 L0 354 Z" fill="var(--gold)"/>
      <path d="M0 82 C60 270 330 290 620 314 L620 354 L0 354 Z" fill="var(--card-white)"/>
      <path d="M0 90 C60 276 330 296 620 320 L620 354 L0 354 Z" fill="var(--royal-blue)"/>
    </svg>
    <div class="front-logo"><span class="logo-dot"></span><span>BDN LTD</span></div>
    <div class="divider"></div>
    <div class="contact">
      <p class="contact-name">Daniel Carter</p>
      <p class="contact-role">Manager</p>
      <p class="contact-address">48 Harbor Lane<br>Millbrook, ST 40215</p>
      <ul class="contact-list">
        <li><svg viewBox="0 0 16 16"><path d="M3 1 L6 1 L7 5 L5 6.5 C6 9 7 10 9.5 11 L11 9 L15 10 L15 13 C15 14 14 15 13 15 C6 15 1 10 1 3 C1 2 2 1 3 1 Z" fill="var(--gold)"/></svg>555-318-4720</li>
        <li><svg viewBox="0 0 16 16"><rect x="1" y="3" width="14" height="10" fill="none" stroke="var(--gold)" stroke-width="1.6"/><path d="M1 3 L8 9 L15 3" fill="none" stroke="var(--gold)" stroke-width="1.6"/></svg>info@bdnltd-mail.com</li>
        <li><svg viewBox="0 0 16 16"><circle cx="8" cy="8" r="6.5" fill="none" stroke="var(--gold)" stroke-width="1.5"/><ellipse cx="8" cy="8" rx="3" ry="6.5" fill="none" stroke="var(--gold)" stroke-width="1.2"/><path d="M1.5 8 H14.5" stroke="var(--gold)" stroke-width="1.2"/></svg>www.bdnltd-build.com</li>
      </ul>
    </div>
  </section>

  <section class="card card-back">
    <div class="back-logo"><span class="logo-dot"></span><span>BDN LTD</span></div>
    <p class="back-web">www.bdnltd-build.com</p>
  </section>
</main>
</body>
</html>
```